edgy fitness flyer

Utilize quote
"I don't want a great body"
by: Nobody Ever
Offer oin back . Vard needs to be edgy and sexy.

Target Market(s)

Women and men 25-45

Industry/Entity Type

Fitness

Requirements
Must have
• clear font layered over gradient image
• See attached sample.
• bright and eye catching
• must coordniate with studio image
• www.vornfitness.com

```html
<!DOCTYPE html>
<html lang="en">
<head>
<meta charset="utf-8">
<title>VORN Fitness Flyer</title>
<link rel="stylesheet" href="https://fonts.googleapis.com/css2?family=Oswald:wght@600;700&family=Open+Sans:wght@700;800&display=swap">
<style>
  :root {
    --ink: #000000;
    --brand-orange: #ec8230;
    --ghost-grey: #383838;
    --quote-white: #f1f1f1;
    --offer-yellow: #ffe500;
    --portrait-light: #e9e9e9;
    --portrait-mid: #6a6a6a;
  }
  html, body {
    margin: 0;
    padding: 0;
    width: 851px;
    height: 1200px;
    overflow: hidden;
    background: var(--ink);
  }
  .flyer {
    display: block;
    width: 851px;
    height: 1200px;
  }
  .brand-ghost {
    font-family: "Oswald", sans-serif;
    font-weight: 700;
    fill: var(--ghost-grey);
  }
  .brand-name {
    font-family: "Oswald", sans-serif;
    font-weight: 700;
    fill: var(--brand-orange);
  }
  .tagline {
    font-family: "Oswald", sans-serif;
    font-weight: 600;
    fill: var(--brand-orange);
  }
  .quote-line {
    font-family: "Open Sans", sans-serif;
    font-weight: 800;
    fill: var(--quote-white);
  }
  .quote-attribution {
    font-family: "Open Sans", sans-serif;
    font-weight: 700;
    fill: var(--quote-white);
  }
  .offer-tab { fill: var(--offer-yellow); }
  .offer-label {
    font-family: "Open Sans", sans-serif;
    font-weight: 800;
    fill: var(--ink);
    letter-spacing: 1px;
  }
  .site-url {
    font-family: "Open Sans", sans-serif;
    font-weight: 700;
    fill: var(--brand-orange);
    letter-spacing: 3px;
  }
</style>
</head>
<body>
<svg class="flyer" viewBox="0 0 851 1200" xmlns="http://www.w3.org/2000/svg">
  <defs>
    <radialGradient id="portrait-glow" cx="0.42" cy="0.52" r="0.55">
      <stop offset="0" stop-color="var(--portrait-light)"/>
      <stop offset="0.35" stop-color="var(--portrait-mid)" stop-opacity="0.7"/>
      <stop offset="1" stop-color="var(--ink)" stop-opacity="0"/>
    </radialGradient>
  </defs>

  <rect width="851" height="1200" fill="var(--ink)"/>

  <text class="brand-ghost" transform="translate(225 1130) rotate(-90)" font-size="300" textLength="1110" lengthAdjust="spacingAndGlyphs">VORN</text>

  <rect class="portrait" role="img" aria-label="Studio portrait of a woman in profile with dark hair and pale skin" x="330" y="420" width="420" height="470" fill="url(#portrait-glow)"/>

  <text class="brand-name" x="30" y="268" font-size="300" textLength="795" lengthAdjust="spacingAndGlyphs">VORN</text>

  <text class="tagline" x="28" y="439" font-size="48" textLength="794" lengthAdjust="spacingAndGlyphs">BUILDING BODIES FROM THE GROUND UP</text>

  <text class="quote-line" x="36" y="926" font-size="80" textLength="630" lengthAdjust="spacingAndGlyphs">"I don't want</text>
  <text class="quote-line" x="120" y="1004" font-size="80" textLength="652" lengthAdjust="spacingAndGlyphs">a great body"</text>
  <text class="quote-attribution" x="372" y="1060" font-size="32" textLength="258" lengthAdjust="spacingAndGlyphs">- Nobody Ever</text>

  <path class="offer-tab" d="M545 1089 H851 V1125 H535 Q533 1125 534 1122 L541 1092 Q542 1089 545 1089 Z"/>
  <text class="offer-label" x="553" y="1117" font-size="26" textLength="272" lengthAdjust="spacingAndGlyphs">OFFER ON BACK</text>

  <text class="site-url" x="425" y="1172" font-size="38" text-anchor="middle" textLength="466" lengthAdjust="spacingAndGlyphs">www.vornfitness.com</text>
</svg>
</body>
</html>
```